Stationary for Home Builder
Larkfield Dwellings Inc.
Project: Stationary for Home Builder
Stationary for Home Builder - Construction
Creative Brief
Modern
Gaston Villemure
Owner
Suite 310-7816 62 Avenue Edmonton, AB T5K 3M2
gaston@larkfielddwellings.ca
larkfielddwellings.ca
The blue colour used in the logo should be replicated and used within the stationary / business cards. Feel free to use additional complementary colours as well (including, but not limited to the grey colour used in the logo).. The intention is to have a modern feel but remain professional. The backside of the card can have designs but should allow some space to write notes.

```html
<!DOCTYPE html>
<html lang="en">
<head>
<meta charset="utf-8">
<title>Larkfield Dwellings Inc. — Stationery</title>
<link href="https://fonts.googleapis.com/css2?family=Roboto:wght@400;500;700&display=swap" rel="stylesheet">
<style>
  :root{
    --blue:#1f74c8;
    --blue-deep:#0f4f98;
    --grey:#8a8d92;
    --charcoal:#46494e;
    --paper:#ffffff;
    --flap-white:#f4f5f6;
    --stage:#ece9e4;
    --ink:#3a3d42;
  }
  *{box-sizing:border-box;margin:0;padding:0}
  html,body{width:1200px;height:600px;overflow:hidden}
  body{background:var(--stage);font-family:'Roboto',Arial,sans-serif;color:var(--ink);position:relative}
  .sheet{position:absolute;background:var(--paper);box-shadow:0 2px 6px rgba(0,0,0,.18);overflow:hidden}
  .brand{display:flex;align-items:center;gap:5px;font-weight:700;color:var(--blue);white-space:nowrap}
  .brand-mark{background:var(--blue);flex:none}
  .decor-band{position:absolute;left:0;bottom:0;width:100%;background:linear-gradient(180deg,var(--grey) 0%,var(--blue) 35%,var(--blue-deep) 100%)}

  /* business cards */
  .card{left:29px;width:139px;height:101px;border-radius:6px}
  .card-front{top:235px}
  .card-back{top:360px}
  .card .brand{position:absolute;top:18px;left:0;right:0;justify-content:center;font-size:8px}
  .card .brand-mark{width:7px;height:7px}
  .card .decor-band{height:34px}
  .card-web{position:absolute;bottom:8px;left:10px;font-size:5px;color:#fff;font-weight:500}

  /* letterhead */
  .letterhead{left:216px;top:29px;width:403px;height:518px}
  .letterhead .brand{position:absolute;top:26px;left:0;right:0;justify-content:center;font-size:15px}
  .letterhead .brand-mark{width:12px;height:12px}
  .letterhead .decor-band{height:84px}
  .letter-contact{position:absolute;left:16px;bottom:14px;list-style:none;font-size:5.5px;line-height:9px;color:#fff}
  .letter-contact li{display:flex;align-items:center;gap:4px}
  .letter-contact i{width:5px;height:5px;background:#fff;border-radius:1px;display:inline-block}

  /* envelopes */
  .envelope{width:410px;height:204px;left:718px}
  .env-blue{top:29px}
  .env-charcoal{top:132px}
  .env-white{top:240px}
  .env-front{left:658px;top:353px;width:448px;height:200px}
  .flap{position:absolute;left:0;top:0;width:100%;height:64px}
  .env-blue .flap{background:var(--blue)}
  .env-charcoal .flap{background:var(--charcoal)}
  .env-white .flap{background:var(--flap-white);border-bottom:1px solid #dfe1e3}
  .envelope .brand{position:absolute;top:20px;left:0;right:0;justify-content:center;font-size:11px}
  .envelope .brand-mark{width:9px;height:9px}
  .env-blue .brand,.env-charcoal .brand{color:#fff}
  .env-blue .brand-mark,.env-charcoal .brand-mark{background:#fff}
  .env-front .brand{position:absolute;top:16px;left:22px;right:auto;justify-content:flex-start}
  .return-address{position:absolute;top:38px;left:22px;font-size:5px;line-height:7px;color:var(--grey)}

  .caption{position:absolute;top:568px;font-size:8px;letter-spacing:1.5px;color:var(--grey)}
  .caption-letter{left:340px}
  .caption-envelope{left:862px}
</style>
</head>
<body>

<div class="sheet card card-front">
  <div class="brand"><span class="brand-mark"></span>Larkfield Dwellings Inc.</div>
  <div class="decor-band" role="img" aria-label="Blue and grey decorative wave band"></div>
  <div class="card-web">larkfielddwellings.ca</div>
</div>

<div class="sheet card card-back">
  <div class="brand"><span class="brand-mark"></span>Larkfield Dwellings Inc.</div>
  <div class="decor-band" role="img" aria-label="Blue and grey decorative wave band"></div>
  <div class="card-web">gaston@larkfielddwellings.ca</div>
</div>

<div class="sheet letterhead">
  <div class="brand"><span class="brand-mark"></span>Larkfield Dwellings Inc.</div>
  <div class="decor-band" role="img" aria-label="Blue and grey decorative wave band"></div>
  <ul class="letter-contact">
    <li><i></i>Gaston Villemure, Owner</li>
    <li><i></i>Suite 310-7816 62 Avenue Edmonton, AB T5K 3M2</li>
    <li><i></i>gaston@larkfielddwellings.ca</li>
    <li><i></i>larkfielddwellings.ca</li>
  </ul>
</div>

<div class="sheet envelope env-blue">
  <div class="flap" role="img" aria-label="Blue decorative envelope flap"></div>
  <div class="brand"><span class="brand-mark"></span>Larkfield Dwellings Inc.</div>
</div>
<div class="sheet envelope env-charcoal">
  <div class="flap" role="img" aria-label="Charcoal decorative envelope flap"></div>
  <div class="brand"><span class="brand-mark"></span>Larkfield Dwellings Inc.</div>
</div>
<div class="sheet envelope env-white">
  <div class="flap" role="img" aria-label="Light grey decorative envelope flap"></div>
  <div class="brand"><span class="brand-mark"></span>Larkfield Dwellings Inc.</div>
</div>
<div class="sheet envelope env-front">
  <div class="brand"><span class="brand-mark"></span>Larkfield Dwellings Inc.</div>
  <div class="return-address">Suite 310-7816 62 Avenue<br>Edmonton, AB T5K 3M2<br>larkfielddwellings.ca</div>
</div>

<div class="caption caption-letter">LETTER-HEAD OPTION 1</div>
<div class="caption caption-envelope">ENVELOPE OPTION 2</div>

</body>
</html>
```